Banner ad for www.brightquiver.example - Online Service for photographers

We need a simple and clean looking banner design that we can use in different formats and contexts online.

We're a new online service for photographers - providing websites, direct picture sales, media management, file delivery and cloud storage.

Our core message is 'Tools for Photographers': Sell Photos - Create Websites - Share Collections

Our target market is professional and 'serious amateur' photographers. We offer free 30 day trials. Members pay monthly or yearly subscriptions.

We're looking for something eye catching, graphically simple and modern that delivers the message clearly.

Required sizes are:

Leader board 728X90
Square pop up - 250x250
Wide skyscraper - 160x600
Button - 120x90
Updates

Target Market(s)

Our core target market is professional and serious amateur/enthusiast photographers.

Industry/Entity Type

Media

Requirements
Must have
• We need our logo

```html
<!DOCTYPE html>
<html lang="en">
<head>
<meta charset="utf-8">
<title>BrightQuiver – Tools for Photographers</title>
<link rel="stylesheet" href="https://fonts.googleapis.com/css2?family=Arimo:wght@400;700&display=swap">
<style>
  :root {
    --ink: #3a3a3a;
    --white: #ffffff;
    --strip-dark: #123a5c;
    --tagline: #5cc8ff;
    --orange-light: #ffb347;
    --orange: #f28a12;
    --orange-deep: #d96400;
    --button-ring: #3b2a1a;
    --photo-warm: #d9925a;
    --photo-mid: #b9745c;
  }
  * { margin: 0; padding: 0; box-sizing: border-box; }
  html, body { width: 1200px; height: 148px; overflow: hidden; background: var(--white); }
  .banner {
    position: relative;
    width: 1200px;
    height: 148px;
    overflow: hidden;
    font-family: "Arimo", Arial, sans-serif;
    background: var(--white);
  }
  .banner__backdrop { position: absolute; inset: 0; }
  .brand {
    position: absolute;
    left: 13px;
    top: 52px;
    display: flex;
    align-items: center;
    gap: 14px;
  }
  .brand__mark {
    width: 42px;
    height: 42px;
    background: var(--ink);
  }
  .brand__name {
    font-size: 40px;
    font-weight: 400;
    color: var(--ink);
    letter-spacing: -0.5px;
    line-height: 1;
  }
  .hero-photo {
    position: absolute;
    left: 330px;
    top: 0;
    width: 240px;
    height: 148px;
    border-radius: 40% 0 0 40% / 50% 0 0 50%;
    background: linear-gradient(90deg, var(--photo-warm) 0%, var(--photo-mid) 55%, rgba(74,165,220,0) 100%);
  }
  .headline {
    position: absolute;
    left: 569px;
    top: 8px;
    font-size: 36px;
    font-weight: 700;
    color: var(--white);
    letter-spacing: 0.2px;
    line-height: 1;
    white-space: nowrap;
  }
  .services {
    position: absolute;
    left: 560px;
    top: 47px;
    width: 604px;
    height: 28px;
    display: flex;
    align-items: center;
    justify-content: space-between;
    padding: 0 10px;
    background: linear-gradient(90deg, rgba(18,58,92,0.55), var(--strip-dark) 20%, var(--strip-dark) 80%, rgba(18,58,92,0.6));
    font-size: 21px;
    color: var(--tagline);
    white-space: nowrap;
  }
  .thumbs {
    position: absolute;
    left: 580px;
    top: 86px;
    width: 310px;
    height: 62px;
  }
  .thumb {
    position: absolute;
    top: 0;
    height: 58px;
    border: 2px solid var(--white);
    box-shadow: 0 2px 4px rgba(0,0,0,0.35);
  }
  .thumb--portrait { left: 0; width: 66px; background: linear-gradient(160deg, #6b4a36, #2e2018); transform: rotate(-4deg); }
  .thumb--temple { left: 70px; width: 76px; background: linear-gradient(180deg, #d7a35a, #8a5a2a); transform: rotate(2deg); top: 2px; }
  .thumb--fabric { left: 146px; width: 78px; background: linear-gradient(160deg, #d13a9a, #7a1f6b); transform: rotate(-3deg); }
  .thumb--seaside { left: 226px; width: 80px; background: linear-gradient(180deg, #c9d6de, #5b6a70); transform: rotate(4deg); top: 2px; }
  .cta {
    position: absolute;
    left: 968px;
    top: 90px;
    width: 176px;
    height: 48px;
    border-radius: 6px;
    background: linear-gradient(180deg, var(--orange-light) 0%, var(--orange) 50%, var(--orange-deep) 100%);
    box-shadow: 0 2px 4px rgba(0,0,0,0.35);
    display: flex;
    align-items: center;
    padding-left: 16px;
    text-decoration: none;
  }
  .cta__label {
    font-size: 21px;
    font-weight: 700;
    color: var(--white);
    text-shadow: 0 1px 2px rgba(0,0,0,0.3);
    white-space: nowrap;
  }
  .cta__icon {
    position: absolute;
    right: 8px;
    top: 6px;
    width: 36px;
    height: 36px;
  }
</style>
</head>
<body>
<div class="banner">
  <svg class="banner__backdrop" width="1200" height="148" viewBox="0 0 1200 148" aria-hidden="true">
    <defs>
      <linearGradient id="sky" x1="0" y1="0" x2="1" y2="1">
        <stop offset="0" stop-color="#9fd3f2"/>
        <stop offset="0.5" stop-color="#4aa5dc"/>
        <stop offset="1" stop-color="#1f6fae"/>
      </linearGradient>
    </defs>
    <rect x="400" y="0" width="800" height="148" fill="url(#sky)"/>
    <path d="M560 148 C700 110 900 120 1200 70 V148 Z" fill="#1f6fae" opacity="0.35"/>
  </svg>

  <div class="brand">
    <span class="brand__mark"></span>
    <span class="brand__name">BrightQuiver</span>
  </div>

  <div class="hero-photo" role="img" aria-label="Photo of a photographer holding a camera"></div>

  <h1 class="headline">TOOLS FOR PHOTOGRAPHERS</h1>

  <p class="services">
    <span>Sell Photos</span><span>-</span><span>Create Websites</span><span>-</span><span>Share Collections</span>
  </p>

  <div class="thumbs">
    <div class="thumb thumb--portrait" role="img" aria-label="Sample portrait photo"></div>
    <div class="thumb thumb--temple" role="img" aria-label="Sample photo of an ancient temple"></div>
    <div class="thumb thumb--fabric" role="img" aria-label="Sample photo of colourful fabric"></div>
    <div class="thumb thumb--seaside" role="img" aria-label="Sample photo of a seaside scene"></div>
  </div>

  <a class="cta" href="#">
    <span class="cta__label">Click Here!</span>
    <svg class="cta__icon" viewBox="0 0 40 40" aria-hidden="true">
      <circle cx="20" cy="20" r="18" fill="#f6a23a" stroke="#3b2a1a" stroke-width="3"/>
      <path d="M16 12 L28 20 L16 28 Z" fill="#3b2a1a"/>
    </svg>
  </a>
</div>
</body>
</html>
```